Deliver a professional and engaging investment propsal.

I am appealing to highend smart investors and need a high quality, engaging and formal presentation in PDF.
StowBin: https://www.stowbin.net/sh/qwmtr48kelvan2x/ZZTrPHmLe7WqsnBFjQ4kR8vYt?dl=0
Text for project is in Stowbin called New Proposal Final
Along with past much older attempts of this job.
Any additional ideas to enable a better outcome would be appreicated.

```html
<!DOCTYPE html>
<html lang="en">
<head>
<meta charset="utf-8">
<title>Kestrel Business Park – Proposal Pages</title>
<link href="https://fonts.googleapis.com/css2?family=Marcellus+SC&family=Saira+Condensed:wght@500&family=Arimo:wght@400;700&display=swap" rel="stylesheet">
<style>
:root{
  --navy:#27226e;
  --violet:#4a1cf6;
  --sky:#5ec2f0;
  --white:#ffffff;
  --ink:#1d1b3a;
  --stage:#000000;
}
*{margin:0;padding:0;box-sizing:border-box}
html,body{width:1200px;height:720px;overflow:hidden;background:var(--stage)}
.board{position:relative;width:1200px;height:720px;font-family:"Arimo",Arial,sans-serif}
.page{position:absolute;background:var(--white)}
.block{position:absolute}
.caps{font-family:"Marcellus SC","Copperplate",serif;letter-spacing:.06em}
.page-label{position:absolute;top:648px;color:var(--white);font-size:29px;font-family:"Arimo",Arial,sans-serif}

/* cover */
.cover{left:12px;top:70px;width:386px;height:562px}
.cover .inner{position:absolute;left:6px;top:5px;width:374px;height:551px;background:var(--navy);overflow:hidden}
.navy{background:var(--navy)}.violet{background:var(--violet)}.sky{background:var(--sky)}
.cover-brand{position:absolute;left:18px;top:20px;font-size:44px;color:var(--sky);letter-spacing:.1em}
.town-photo{position:absolute;left:0;top:75px;width:374px;height:189px;background:linear-gradient(180deg,#3b6fb8 0%,#6d8fc4 45%,#c07a4a 75%,#3a2b2a 100%)}
.cover-park{position:absolute;left:0;width:374px;top:222px;text-align:center;font-size:34px;color:var(--sky);letter-spacing:.05em}
.acre{position:absolute;left:136px;top:272px;font-size:40px;color:var(--white);letter-spacing:.08em}
.mixed{position:absolute;left:136px;top:325px;font-size:14px;color:var(--sky)}
.sign-photo{position:absolute;left:0;top:351px;width:352px;height:107px;background:linear-gradient(180deg,#8d8d8d,#cfcfcf 50%,#7a7a7a)}
.road-strip{position:absolute;left:0;top:529px;width:374px;height:22px;background:linear-gradient(90deg,#6f6a66,#a09b95,#6f6a66)}
.cover-title{position:absolute;left:18px;top:466px;font-size:25px;line-height:32px;color:var(--white)}

/* contents */
.contents{left:406px;top:68px;width:374px;height:566px}
.contents .inner{position:absolute;left:5px;top:13px;width:364px;height:540px;overflow:hidden;background:linear-gradient(180deg,#e8ecf6 0%,#cfd4de 25%,#9b968c 45%,#a9a59d 70%,#cfcbc4 100%)}
.contents-title{position:absolute;left:0;width:374px;top:18px;text-align:center;font-family:"Saira Condensed","Arial Narrow",sans-serif;font-weight:500;font-size:40px;line-height:44px}
.contents-title .dark{color:var(--navy)}.contents-title .bright{color:var(--violet)}
.contents-sub{position:absolute;left:0;width:374px;top:62px;text-align:center;font-size:16px;color:var(--navy)}
.toc-row{position:absolute;left:4px;width:322px;height:71px;display:flex}
.toc-num{width:80px;background:var(--violet);color:var(--white);font-family:"Arimo",Arial,sans-serif;font-size:30px;display:flex;align-items:center;padding-left:26px}
.toc-name{flex:1;background:var(--navy);color:var(--white);display:flex;align-items:center;padding-left:14px;font-size:14px;line-height:15px}
.toc-name.center{justify-content:center;text-align:center;padding-left:0}

/* proposal page */
.proposal{left:790px;top:68px;width:386px;height:566px}
.head-bar{position:absolute;left:6px;top:6px;width:282px;height:70px;background:var(--violet);color:var(--white);font-size:25px;display:flex;align-items:center;padding-left:48px;letter-spacing:.1em}
.head-num{position:absolute;left:288px;top:6px;width:92px;height:70px;background:var(--navy);color:var(--white);font-size:30px;display:flex;align-items:center;justify-content:center}
.intro{position:absolute;left:18px;top:81px;width:356px;font-size:7.3px;font-weight:700;line-height:8.8px;color:var(--ink)}
.intro p{margin-bottom:9px}
.options-title{position:absolute;left:18px;top:170px;font-size:14px;color:var(--violet);font-family:"Arimo",Arial,sans-serif}
.option{position:absolute;background:var(--navy);color:var(--white);font-size:6.2px;line-height:9.6px;padding:16px 6px 4px;border-bottom:4px solid var(--violet)}
.option.dense{line-height:8.6px}
.option b{font-weight:700}
.option-num{position:absolute;top:-13px;left:50%;margin-left:-13px;width:26px;height:26px;border-radius:50%;background:var(--violet);border:2px solid var(--white);color:var(--white);font-size:16px;font-weight:700;display:flex;align-items:center;justify-content:center}
.option::after{content:"";position:absolute;left:50%;bottom:-11px;margin-left:-7px;border-left:7px solid transparent;border-right:7px solid transparent;border-top:7px solid var(--navy)}
</style>
</head>
<body>
<div class="board">

  <section class="page cover">
    <div class="inner">
      <div class="block sky" style="left:266px;top:0;width:108px;height:75px"></div>
      <div class="block violet" style="left:266px;top:24px;width:100px;height:17px"></div>
      <div class="block violet" style="left:350px;top:24px;width:16px;height:51px"></div>
      <div class="cover-brand caps">Kestrel</div>
      <div class="town-photo" role="img" aria-label="Evening photograph of a small-town main street with lit storefronts"></div>
      <div class="cover-park caps">Business Park</div>
      <div class="block sky" style="left:0;top:264px;width:114px;height:87px"></div>
      <div class="block violet" style="left:0;top:264px;width:18px;height:56px"></div>
      <div class="block violet" style="left:0;top:320px;width:114px;height:14px"></div>
      <div class="acre caps">60 Acre</div>
      <div class="mixed caps">Mixed-Used Development</div>
      <div class="sign-photo" role="img" aria-label="Photograph of a weathered Welcome to Dunmore Falls town sign"></div>
      <div class="block violet" style="left:352px;top:351px;width:22px;height:178px"></div>
      <div class="block sky" style="left:234px;top:458px;width:118px;height:20px"></div>
      <div class="block violet" style="left:234px;top:478px;width:140px;height:30px"></div>
      <div class="cover-title caps">Project<br>Proposal</div>
      <div class="road-strip" role="img" aria-label="Photograph of a road surface"></div>
    </div>
  </section>

  <section class="page contents">
    <div class="inner" role="img" aria-label="Photograph of a long straight prairie highway under a pale sky"></div>
    <h1 class="contents-title"><span class="dark">KESTREL</span> <span class="bright">BUSINESS PARK</span></h1>
    <div class="contents-sub caps">Contents</div>
    <div class="toc-row" style="top:86px"><div class="toc-num">1</div><div class="toc-name caps" style="font-size:22px">Proposal</div></div>
    <div class="toc-row" style="top:184px"><div class="toc-num">2</div><div class="toc-name caps" style="font-size:16px">Major Site Changes</div></div>
    <div class="toc-row" style="top:282px"><div class="toc-num">3</div><div class="toc-name caps" style="font-size:16px">Locations</div></div>
    <div class="toc-row" style="top:386px"><div class="toc-num">4</div><div class="toc-name center caps" style="font-size:12px">Summit Lodge Plus Extended<br>Stay/ Sensitivity Analysis</div></div>
    <div class="toc-row" style="top:489px"><div class="toc-num" style="padding-left:14px;font-size:26px">5-6</div><div class="toc-name center caps" style="font-size:13px">About Our Quality Team<br>In Conclusion</div></div>
  </section>

  <section class="page proposal">
    <div class="head-bar caps">Proposal</div>
    <div class="head-num">1</div>
    <div class="intro">
      <p>We have an incredible property, Kestrel Business Park, located at 1180 Prairie Route 40 Harlan County, Dunmore Falls, North Dakota 58999 USA which we have fully funded with cash and now need a joint venture partner, buyer or lender to get this project to completion and producing a substantial profit we all can share.</p>
      <p>Our property is located on the best oil reserves in the world in North Dakota USA, with more oil than any other county in the Bakken Basin and with the lowest recoverable costs of $24 a barrel.</p>
      <p>We own the property and need a partner to develop the site and bring to the market at half</p>
    </div>
    <h2 class="options-title">Participation Options</h2>

    <div class="option" style="left:20px;top:194px;width:88px;height:100px"><div class="option-num">1</div><b>A joint venture partner</b> would support all the costs developing the property without the upfront costs of the property purchase.</div>
    <div class="option" style="left:136px;top:194px;width:96px;height:102px"><div class="option-num">2</div>All sales would be split to ensure both parties are paid out in such a way that both are paid out in full at the same time then a 50/50 profit share split on all remaining sales.</div>
    <div class="option" style="left:258px;top:194px;width:94px;height:102px"><div class="option-num">3</div><br>Contract drawn up protecting and supporting both parties on agreed terms.</div>

    <div class="option dense" style="left:16px;top:326px;width:96px;height:98px"><div class="option-num">4</div>As a potential joint venture partner, I would cover the full property (57.7 acres) cost as mentioned of $124,784 per acre (57.7 acres). ($7,200,000)</div>
    <div class="option dense" style="left:136px;top:326px;width:96px;height:98px"><div class="option-num">5</div>Joint venture partner to supply the development costs estimated to be around $65,000 an acre estimated pending tender selection and additional refundable security bonds held with the Dunmore Falls on development works.</div>
    <div class="option" style="left:250px;top:326px;width:96px;height:98px"><div class="option-num">6</div>Development costs could be in up to three stages to lower outlay and limit exposure if so desired, however it will take longer to complete and bring to market.</div>

    <div class="option" style="left:19px;top:454px;width:90px;height:98px"><div class="option-num">7</div><b>A buyer</b> can be fully supported by myself to oversee the full project and outcomes and support the budgets of construction and sales to get the highest returns for a small fee.</div>
    <div class="option" style="left:136px;top:454px;width:96px;height:98px"><div class="option-num">8</div>To purchase the property, you would need to contact me directly and I can introduce you to our realtor who will discount his commission from 6% to 5% which is a significant saving.</div>
    <div class="option" style="left:247px;top:454px;width:96px;height:98px"><div class="option-num">9</div><br><b>Financing</b> on excellent terms allowing 12 to 18 months for income streams and could be linked to a joint venture option / profit share.</div>
  </section>

  <div class="page-label" style="left:17px">Cover</div>
  <div class="page-label" style="left:408px">Table of content</div>
  <div class="page-label" style="left:804px">Page 1</div>
</div>
</body>
</html>
```